IT Tradingsystem for car dealers needs Business Card Design

We need a fresh and modern design for our new business cards.

We develop a it-business system for car dealers in Sweden, Norway and on our way down to further countries in Europe, hence the namechange to BrolaTek Europe AB. The site can be found at www.brolatek-example.com. The startpage is also in for an update/modernization soon so don't take to much from here.

We are looking to print double sided, 4-colour cards.

We want to look professional, modern and serious. Open to cooler suggestions, but not too crazy. We need to make a good and serious impression on our potential customers. It needs to reflect our scandinavian design values and layout.

Preferably with the full BrolaTek logo in good size on the back, so the small print on the logo can be read easily.

Text that needs to go on the cards:
-------

Per Oskar Fjellström
Founder

Direct +46 70-512 96 47
Support 08-612 57 394
po.fjellstrom@brolatek-example.com

BrolaTek Europe AB
Box 8617
104 29 Stockholm

Brolatek-example.com
Saljportalen-example.se

--------
Good luck and thanks!

PS. If you need more input or see what our previous cards looked like, don't hesitate to contact me!

Target Market(s)

Decision makers / executives at brand cardealers

Industry/Entity Type

Automotive

Contact Information for Business Card

Normal size

Requirements
Must have
• Full logo
Nice to have
• Base on our orange colors
Should not have
• No fonts with serif, and not too much graphics

```html
<!DOCTYPE html>
<html lang="sv">
<head>
<meta charset="utf-8">
<title>BrolaTek – visitkort</title>
<link rel="stylesheet" href="https://fonts.googleapis.com/css2?family=Roboto:wght@400;700&family=Lato:wght@400;700&display=swap">
<style>
  :root {
    --board: #222222;
    --orange: #F47B20;
    --ink: #231F20;
    --paper: #FFFFFF;
  }
  * { margin: 0; padding: 0; box-sizing: border-box; }
  html, body { width: 1189px; height: 1200px; overflow: hidden; background: var(--board); }
  .canvas { position: relative; width: 1189px; height: 1200px; }
  .card { position: absolute; left: 171px; width: 856px; height: 488px; overflow: hidden; }
  .card--back { top: 67px; background: var(--orange); color: var(--paper); }
  .card--front { top: 626px; background: var(--paper); color: var(--ink); }

  .wordmark { position: absolute; font-family: "Roboto", sans-serif; font-weight: 700; letter-spacing: -1px; line-height: 1; }
  .tagline { position: absolute; font-family: "Roboto", sans-serif; font-weight: 400; letter-spacing: 1px; line-height: 1; white-space: nowrap; }

  .card--back .wordmark { left: 268px; top: 203px; font-size: 76px; }
  .card--back .tagline { left: 270px; top: 276px; font-size: 21px; }
  .card--back .web { position: absolute; left: 0; right: 0; top: 384px; text-align: center; font-family: "Lato", sans-serif; font-size: 22px; }

  .brand-tab { position: absolute; left: 52px; top: 0; width: 105px; height: 160px; background: var(--orange); }
  .card--front .wordmark { left: 176px; top: 81px; font-size: 70px; color: var(--ink); }
  .card--front .tagline { left: 178px; top: 150px; font-size: 20px; color: var(--ink); }

  .person { position: absolute; left: 51px; top: 268px; font-family: "Lato", sans-serif; }
  .person__name { font-weight: 700; font-size: 29px; line-height: 1.05; }
  .person__title { font-size: 22px; color: var(--orange); line-height: 1.1; }

  .contact, .address { position: absolute; top: 372px; font-family: "Lato", sans-serif; font-size: 23px; line-height: 28.5px; list-style: none; white-space: nowrap; }
  .contact { left: 52px; }
  .contact__label { color: var(--orange); }
  .address { left: 566px; top: 375px; }
</style>
</head>
<body>
<main class="canvas">
  <section class="card card--back" aria-label="Kortets baksida">
    <div class="wordmark">BrolaTek</div>
    <div class="tagline">Provkoll &nbsp;|&nbsp; Remarketing &nbsp;|&nbsp; saljportalen-example.se</div>
    <p class="web">www.Brolatek-example.com | www.Saljportalen-example.se</p>
  </section>

  <section class="card card--front" aria-label="Kortets framsida">
    <div class="brand-tab"></div>
    <div class="wordmark">BrolaTek</div>
    <div class="tagline">Provkoll &nbsp;|&nbsp; Remarketing &nbsp;|&nbsp; saljportalen-example.se</div>

    <div class="person">
      <p class="person__name">Per Oskar Fjellström</p>
      <p class="person__title">Founder</p>
    </div>

    <ul class="contact">
      <li><span class="contact__label">Direct:</span> +46 70-512 96 47</li>
      <li><span class="contact__label">Support</span> 08-612 57 394</li>
      <li><span class="contact__label">E:</span> po.fjellstrom@brolatek-example.com</li>
    </ul>

    <ul class="address">
      <li>BrolaTek Europe AB</li>
      <li>Box 8617</li>
      <li>104 29 Stockholm</li>
    </ul>
  </section>
</main>
</body>
</html>
```